A new book about Surrogacy and infertility

Im a medical doctor and writing a book about Surrogacy and infertility around the world. The book will be mainly a non-fictional book, but there will also be some personal stories from surrogatemothers and intended mothers. In looking for a clean design with focus on a non-fictional type of book with focus on facts. The book will cover the scientific studies done on Surrogacy, surrogacy around the world from USA to India and also reveal some of the myths about surrogacy.

I would like the design to show surrogacy and global infertility, so that the reader hopefully can see what the book is about only from looking at the graphics on the book cover. Im open for all kinds of ideas and symbolic designs. Maybe pregnant women with a globe, preferably not only caucasian women on the design since the book will cover alot of surrogcy in India, but also other countries.

The book is written in Swedish and the main title is "Ljusbärarinnan"
the subtitle is: Stjärnregnet under "höstvind"
Author:"Fredrik Holmqvist"
The book format will be in A5 on the backside reviews of the book will be placed and a small picture and description of the author and an EAN bar
Updates

Hi!

Thanks for all the designs so far, some of them look great. Still looking for more designs. I have updated the brief now so hopefully its more clear what Im looking for. I also have given some feedback to all the designers who have submitted designs.

Thanks alot

Fredrik Holmqvist

Target Market(s)

The book will cover more hard facts about surrogacy then being a personal story about becoming parent. It will cover both good and bad examples of surrogacy in different countries. A design for a non-fictional book with facts covering surrogacy and infertility.

Industry/Entity Type

Medical

Font styles to use
Serif
Sans Serif

Colors

Designer to choose colors to be used in the design.

Requirements
Nice to have
• Book cover should show surrogacy and global infertility in the graphics. Could be symbolic or with pictures. A pregnant women and a globe is one idea but Im open to many suggestions. Preferably not only designs with caucasian women.

```html
<!DOCTYPE html>
<html lang="sv">
<head>
<meta charset="utf-8">
<title>Ljusbärarinnan – bokomslag</title>
<link rel="stylesheet" href="https://fonts.googleapis.com/css2?family=Teko:wght@500;600&family=Questrial&display=swap">
<style>
  :root {
    --page-bg: #e6e7e9;
    --cover-bg: #f1f2f3;
    --title-blue: #1f6f9a;
    --deep-blue: #175c82;
    --box-text: #c9dbe6;
    --photo-top: #eeedf3;
    --photo-top-shade: #d9d8e2;
    --photo-skin: #e9c4aa;
    --photo-skin-mid: #dcae93;
    --photo-shade: #c8957a;
    --photo-bottom: #e4e2ea;
  }
  * { margin: 0; padding: 0; box-sizing: border-box; }
  html, body { width: 1200px; height: 800px; overflow: hidden; }
  body { background: var(--page-bg); position: relative; font-family: "Questrial", sans-serif; }

  .book-wrap {
    position: absolute; left: 130px; top: 80px;
    display: flex; height: 640px;
    box-shadow: 0 12px 30px rgba(0,0,0,0.12);
  }
  .cover { width: 450px; height: 640px; background: var(--cover-bg); position: relative; overflow: hidden; }
  .spine {
    width: 40px; height: 640px; background: var(--cover-bg);
    border-left: 1px solid #d9dbde; border-right: 1px solid #d9dbde;
    display: flex; flex-direction: column; align-items: center; justify-content: space-between;
    padding: 14px 0;
  }
  .spine-title, .spine-author {
    writing-mode: vertical-rl; font-family: "Teko", sans-serif; color: var(--title-blue);
    text-transform: uppercase;
  }
  .spine-title { font-size: 34px; letter-spacing: 6px; font-weight: 600; line-height: 1; }
  .spine-author { font-size: 13px; letter-spacing: 2px; color: var(--deep-blue); }

  .title {
    font-family: "Teko", sans-serif; font-weight: 600; color: var(--title-blue);
    text-transform: uppercase; line-height: 0.9; text-align: center;
  }
  .subtitle {
    font-family: "Teko", sans-serif; font-weight: 500; color: var(--deep-blue);
    text-transform: uppercase; text-align: center; line-height: 1;
  }

  /* Back cover */
  .back .author-top {
    position: absolute; right: 34px; top: 26px;
    font-family: "Teko", sans-serif; font-size: 15px; letter-spacing: 1px;
    color: var(--deep-blue); text-transform: uppercase;
  }
  .back .title { position: absolute; left: 24px; right: 24px; top: 44px; font-size: 58px; }
  .back .subtitle { position: absolute; left: 24px; right: 24px; top: 100px; font-size: 21px; letter-spacing: 4px; }
  .back .blurb {
    position: absolute; left: 24px; right: 24px; top: 134px;
    font-size: 12px; line-height: 1.42; color: var(--deep-blue); text-align: justify;
  }
  .info-box {
    position: absolute; bottom: 28px; width: 100px; height: 58px; background: var(--deep-blue);
    color: var(--box-text); font-size: 11px; display: flex; align-items: center; justify-content: center;
  }
  .isbn-box { left: 38px; }
  .logo-box { right: 34px; }

  /* Front cover */
  .front .title { position: absolute; left: 14px; right: 14px; top: 30px; font-size: 66px; }
  .front .subtitle { position: absolute; left: 14px; right: 14px; top: 92px; font-size: 24px; letter-spacing: 4px; }
  .cover-photo {
    position: absolute; left: 0; top: 132px; width: 400px; bottom: 0;
    background:
      radial-gradient(ellipse 70% 34% at 55% 58%, rgba(255,232,214,0.55) 0%, rgba(255,232,214,0) 70%),
      linear-gradient(180deg,
        var(--photo-skin-mid) 0%,
        var(--photo-top) 4%,
        var(--photo-top-shade) 26%,
        var(--photo-top) 32%,
        var(--photo-skin) 38%,
        var(--photo-skin-mid) 60%,
        var(--photo-shade) 78%,
        var(--photo-skin-mid) 86%,
        var(--photo-bottom) 90%,
        var(--photo-top) 100%);
  }
  .front .author-bottom {
    position: absolute; right: 24px; bottom: 44px;
    font-family: "Teko", sans-serif; font-size: 17px; letter-spacing: 1.5px;
    color: var(--deep-blue); text-transform: uppercase;
  }
</style>
</head>
<body>
  <div class="book-wrap">
    <section class="cover back">
      <div class="author-top">Fredrik Holmqvist</div>
      <h2 class="title">Ljusbärarinnan</h2>
      <div class="subtitle">Stjärnregnet under "höstvind"</div>
      <p class="blurb">Lorem ipsum dolor sit amet, consectetur adipisicing elit, sed do eiusmod tempor incididunt ut labore et dolore magna aliqua. Ut enim ad minim veniam, quis nostrud exercitation. Lorem ipsum dolor sit amet, consectetur adipisicing elit, sed do eiusmod tempor incididunt ut labore et dolore magna aliqua. Ut enim ad minim veniam, quis nostrud exercitation. Lorem ipsum dolor sit amet, consectetur adipisicing elit, sed do eiusmod tempor incididunt ut labore et dolore magna aliqua. Ut enim ad minim veniam, quis nostrud exercitation. Lorem ipsum dolor sit amet, consectetur adipisicing elit, sed do eiusmod tempor incididunt ut labore et dolore magna aliqua. Ut enim ad minim veniam, quis nostrud exercitation. Lorem ipsum dolor sit amet, consectetur adipisicing elit, sed do eiusmod tempor incididunt ut labore et dolore magna aliqua. Ut enim ad minim veniam, quis nostrud exercitation. Lorem ipsum dolor sit amet, consectetur adipisicing elit, sed do eiusmod tempor incididunt ut labore et dolore magna aliqua. Ut enim ad minim veniam, quis nostrud exercitation. Lorem ipsum dolor sit amet, consectetur adipisicing elit, sed do eiusmod tempor incididunt ut labore et dolore magna aliqua. Ut enim ad minim veniam, quis nostrud exercitation. Lorem ipsum dolor sit amet, consectetur adipisicing elit, sed do eiusmod tempor incididunt ut labore et dolore magna aliqua. Ut enim ad minim veniam, quis nostrud exercitation. Lorem ipsum dolor sit amet, consectetur adipisicing elit, sed do eiusmod tempor incididunt ut labore et dolore magna aliqua. Ut enim ad minim veniam, quis nostrud exercitation.</p>
      <div class="info-box isbn-box">ISBN</div>
      <div class="info-box logo-box">LOGO</div>
    </section>

    <div class="spine">
      <span class="spine-title">Ljusbärarinnan</span>
      <span class="spine-author">Fredrik Holmqvist</span>
    </div>

    <section class="cover front">
      <h1 class="title">Ljusbärarinnan</h1>
      <div class="subtitle">Stjärnregnet under "höstvind"</div>
      <div class="cover-photo" role="img" aria-label="Photograph of a pregnant woman's belly in a white top and white trousers, her hands resting on the bump"></div>
      <div class="author-bottom">Fredrik Holmqvist</div>
    </section>
  </div>
</body>
</html>
```